Birchline Septic Solutions

Would like to see some single sided ones but would also like to see some double sided with one sided only being the logo. Owners name is Tom Halvick. Phone number is 555-214-0387
Services are pumping, inspections, installs, and repairs

Contact Information for Business Card

555-241-0387 Tom Halvick Larkmoor, ME

```html
<!DOCTYPE html>
<html lang="en">
<head>
<meta charset="utf-8">
<title>Birchline Septic Solutions – Business Cards</title>
<link rel="stylesheet" href="https://fonts.googleapis.com/css2?family=Montserrat:wght@500;700;800&display=swap">
<style>
  :root {
    --canvas: #2a2a2d;
    --card: #1c1c1e;
    --teal: #2bb7b3;
    --white: #ffffff;
    --emboss: #2b2b2e;
  }
  * { margin: 0; padding: 0; box-sizing: border-box; }
  html, body {
    width: 1200px; height: 948px; overflow: hidden;
    background: var(--canvas);
    font-family: "Montserrat", sans-serif;
  }
  .sheet { position: relative; width: 1200px; height: 948px; }

  .card {
    position: absolute;
    width: 700px; height: 400px;
    background: var(--card);
    border-radius: 22px;
    border-bottom: 6px solid var(--teal);
    overflow: hidden;
  }
  .card--back { left: 250px; top: 54px; }
  .card--front { left: 250px; top: 494px; }

  .wordmark {
    position: absolute; left: 0; right: 0;
    text-align: center;
    font-weight: 800;
    text-transform: uppercase;
    line-height: 1;
  }
  .wordmark__name { display: block; font-size: 64px; letter-spacing: 2px; }
  .wordmark__tag { display: block; font-size: 17px; letter-spacing: 9px; margin-top: 12px; }

  .card--back .wordmark { top: 140px; color: var(--emboss); }
  .card--front .wordmark { top: 60px; color: var(--white); }
  .card--front .wordmark__name { font-size: 52px; }
  .card--front .wordmark__tag { font-size: 14px; letter-spacing: 8px; margin-top: 10px; }

  .contact {
    position: absolute; left: 0; right: 0; top: 178px;
    display: flex; justify-content: center; align-items: center; gap: 26px;
  }
  .person { text-align: right; }
  .person__name {
    font-weight: 800; font-size: 30px; color: var(--teal);
    text-transform: uppercase; letter-spacing: 0.5px; line-height: 1.05;
  }
  .person__place { font-weight: 500; font-size: 17px; color: var(--white); margin-top: 4px; }
  .divider { width: 1px; height: 64px; background: var(--teal); }
  .phone {
    display: flex; align-items: center; gap: 10px;
    font-weight: 500; font-size: 24px; color: var(--white);
  }
  .phone svg { width: 20px; height: 20px; fill: var(--teal); }

  .bands { position: absolute; left: 0; bottom: 0; width: 700px; height: 120px; }
</style>
</head>
<body>
<main class="sheet">

  <section class="card card--back" aria-label="Business card back">
    <div class="wordmark">
      <span class="wordmark__name">Birchline</span>
      <span class="wordmark__tag">Septic Solutions</span>
    </div>
  </section>

  <section class="card card--front" aria-label="Business card front">
    <div class="wordmark">
      <span class="wordmark__name">Birchline</span>
      <span class="wordmark__tag">Septic Solutions</span>
    </div>

    <div class="contact">
      <div class="person">
        <div class="person__name">Tom Halvick</div>
        <div class="person__place">Larkmoor, ME</div>
      </div>
      <div class="divider"></div>
      <div class="phone">
        <svg viewBox="0 0 24 24" aria-hidden="true"><path d="M6.6 10.8a15.1 15.1 0 0 0 6.6 6.6l2.2-2.2a1 1 0 0 1 1-.25 11.4 11.4 0 0 0 3.6.57 1 1 0 0 1 1 1V20a1 1 0 0 1-1 1A17 17 0 0 1 3 4a1 1 0 0 1 1-1h3.5a1 1 0 0 1 1 1c0 1.25.2 2.46.57 3.6a1 1 0 0 1-.25 1z"/></svg>
        <span>555-241-0387</span>
      </div>
    </div>

    <svg class="bands" viewBox="0 0 700 120" aria-hidden="true">
      <polygon class="band-white" points="0,90 372,90 354,114 0,114" fill="var(--white)"/>
      <polygon class="band-teal" points="384,90 408,40 700,40 700,90" fill="var(--teal)"/>
    </svg>
  </section>

</main>
</body>
</html>
```